Trifold Brochure needed for Elm Path Counseling

Hi! We need to have a trifold brochure made.

We would like to see brochure designs that use our logo colors, which are khaki, chocolate brown, and gray.

The brochure should be a modern design and please use your creativity.

Brochure is a trifold brochure, size is 8.5 x 11 and full color.

The following attachment has the content to be used in the trifold brochure, as well as some possible pictures. I have also attached our logo.

We would like to use file #2 for sure (picture number 27193540) and add the quote from her...

"At first, I was reluctant about going to ElmPath. Once I got there, I was glad I went. I learned a lot and was treated like family the whole time." Maren Colby

Requirements
Must have
• Our logo
• Information should be listed exactly as the attached document
• You must stick with our logo colors

```html
<!DOCTYPE html>
<html lang="en">
<head>
<meta charset="utf-8">
<title>ElmPath Counseling – Trifold Brochure</title>
<link href="https://fonts.googleapis.com/css2?family=Questrial&display=swap" rel="stylesheet">
<style>
  :root {
    --chocolate: #5d3815;
    --blush: #fbeee9;
    --ink: #4a2a10;
    --paper: #ffffff;
    --backdrop: #f2f2f2;
  }
  * { margin: 0; padding: 0; box-sizing: border-box; }
  html, body { width: 1200px; height: 1000px; overflow: hidden; }
  body { background: var(--backdrop); font-family: "Questrial", "Century Gothic", sans-serif; color: var(--ink); }
  .canvas { position: relative; width: 1200px; height: 1000px; }
  .brochure {
    position: absolute; left: 70px; top: 168px;
    width: 990px; height: 621px;
    transform: scale(1.07); transform-origin: top left;
    background: var(--paper);
  }
  .block { position: absolute; }
  .blush { background: var(--blush); }
  .chocolate { background: var(--chocolate); }
  .rule { position: absolute; background: var(--chocolate); }

  .brand-title { position: absolute; left: 20px; top: 17px; font-size: 19px; color: var(--ink); }
  .intro { position: absolute; left: 20px; top: 48px; width: 292px; font-size: 11px; line-height: 16px; text-align: justify; }

  .band-heading { position: absolute; color: #fff; font-size: 15px; letter-spacing: .2px; display: flex; align-items: center; }
  .sub-heading { position: absolute; font-size: 15px; color: var(--ink); }
  .body-copy { position: absolute; font-size: 11px; line-height: 16px; }
  .body-copy p + p { margin-top: 4px; }

  .bullets { position: absolute; list-style: none; font-size: 11px; line-height: 16px; text-align: justify; }
  .bullets li { position: relative; padding-left: 17px; margin-bottom: 9px; }
  .bullets li::before { content: ""; position: absolute; left: 1px; top: 5px; width: 7px; height: 7px; border-radius: 50%; background: var(--chocolate); }
  .bullets.spaced li { margin-bottom: 16px; }

  .photo { position: absolute; }
  .photo-autumn { background: linear-gradient(160deg, #c9b79a 0%, #8a6a4a 55%, #9a4a1e 100%); }
  .photo-park { background: linear-gradient(170deg, #b9c79a 0%, #d9b49a 50%, #c86a4a 100%); }
  .photo-bikes { background: linear-gradient(165deg, #a9c77a 0%, #cfd9b0 45%, #d98a8a 100%); }

  .promise { position: absolute; color: #fff; text-align: center; font-size: 15px; line-height: 17px; }
  .promise strong { font-weight: normal; }
  .ripple { position: absolute; color: #fff; font-size: 15px; line-height: 17px; text-align: justify; }
</style>
</head>
<body>
<div class="canvas">
  <div class="brochure">
    <!-- Panel one -->
    <div class="rule" style="left:5px; top:3px; width:322px; height:5px;"></div>
    <div class="block blush" style="left:5px; top:8px; width:322px; height:125px;">
      <div class="brand-title">ElmPath</div>
      <p class="intro">is Pro-active Opioid Education not for addicts or problem patients. ElmPath only sees Good Patients, because problem patients and addicts do not want education they only want pills.</p>
    </div>
    <div class="block chocolate band-heading" style="left:5px; top:137px; width:322px; height:30px; padding-left:16px;">WE EDUCATE GOOD PATIENTS</div>
    <div class="block blush" style="left:5px; top:167px; width:322px; height:283px;"></div>
    <div class="sub-heading" style="left:20px; top:170px;">BECAUSE</div>
    <div class="body-copy" style="left:21px; top:200px; width:294px;">
      <p>Good patients are receptive to new information.</p>
      <p>“Education” Good Patients need it the least! Therefore their minds are open and will soak it up the Most.</p>
    </div>
    <div class="photo photo-autumn" role="img" aria-label="Photo of a smiling senior couple lying in autumn leaves" style="left:20px; top:280px; width:292px; height:166px;"></div>

    <!-- Panel two -->
    <div class="block chocolate band-heading" style="left:333px; top:5px; width:321px; height:29px; padding-left:27px;">EDUCATION HELPS ….</div>
    <div class="block blush" style="left:333px; top:34px; width:321px; height:416px;"></div>
    <ul class="bullets" style="left:342px; top:48px; width:298px;">
      <li>Education helps patient understand, predict and manage their pain cycles.</li>
      <li>Education helps lessen negative thinking and emotional stress</li>
      <li>Education coping skills to minimize pain and to maximize active involvement in positive like experiences.</li>
      <li>Educating Your Patients will mean more effective use of your medical services, meaning fewer unnecessary phone calls to your staff.</li>
      <li>Equals improved Compliance, which means more Compliant urine drug screens.</li>
    </ul>
    <div class="photo photo-park" role="img" aria-label="Photo of a happy senior couple embracing in a park" style="left:349px; top:275px; width:291px; height:171px;"></div>

    <!-- Bottom band across panels one and two -->
    <div class="block chocolate" style="left:5px; top:450px; width:651px; height:166px;"></div>
    <p class="promise" style="left:30px; top:489px; width:272px;"><strong>ElmPath</strong> will teach you and hopefully you will teach someone else, better than that, maybe your education will save someone else.</p>
    <p class="ripple" style="left:351px; top:472px; width:287px;">One Patient’s Education Can Positively Affect A Family; That One Family Can Positively Affect One Neighborhood: One Neighborhood Can Positively Affect One Community; One Community At A Time, Can Change Society.</p>

    <!-- Panel three -->
    <div class="block chocolate band-heading" style="left:654px; top:5px; width:330px; height:29px; padding-left:34px; padding-top:8px;">WHO WE ARE</div>
    <div class="block blush" style="left:654px; top:34px; width:330px; height:579px;"></div>
    <div class="sub-heading" style="left:688px; top:36px;">AND WHAT WE DO ?</div>
    <ul class="bullets spaced" style="left:669px; top:90px; width:300px;">
      <li>ElmPath Counseling provides pro-active counseling, opioid education to the Patient and a Risk Management service to the Physician.</li>
      <li>We believe it starts with giving Education to good patients and letting it trickle down to patients and friends they know, who could use the information too.</li>
      <li>ElmPath helps the physicians by ensuring that the Patients are fully Educated and taking more responsibility for their treatment.</li>
    </ul>
    <div class="photo photo-bikes" role="img" aria-label="Photo of a laughing senior couple riding bicycles outdoors" style="left:677px; top:361px; width:292px; height:252px;"></div>
    <div class="rule" style="left:656px; top:613px; width:328px; height:3px;"></div>
  </div>
</div>
</body>
</html>
```